Tulmex Business Card

I already have the conplay logo. I need to develop a professional business card layout

Target Market(s)

Business

Industry/Entity Type

Business

Contact Information for Business Card

Company Name: Tulmex Limited

Font styles to use
Sans Serif

Colors

Designer to choose colors to be used in the design.

Requirements
Must have
• Use current logo
• Need two card size options:
• Small Card: 70mm x 28mm (Landscape)
• Square Card: 65mm x 65mm
Nice to have
• I will need 8-10 files for each name, number and email address (details to follow)

```html
<!DOCTYPE html>
<html lang="en">
<head>
<meta charset="utf-8">
<title>Tulmex Business Card</title>
<link href="https://fonts.googleapis.com/css2?family=Lato:wght@400;700;900&display=swap" rel="stylesheet">
<style>
  :root {
    --page: #e9e7e4;
    --card: #0c0c0c;
    --card-edge: #1a1a1a;
    --green: #8cc63f;
    --text: #e6e6e6;
    --muted: #6b6b6b;
    --silver: #cfcfcf;
  }
  * { margin: 0; padding: 0; box-sizing: border-box; }
  html, body { width: 1200px; height: 900px; overflow: hidden; }
  body {
    background: var(--page);
    font-family: "Lato", Arial, sans-serif;
    position: relative;
  }
  .card {
    position: absolute;
    background: var(--card);
    border: 1px solid var(--card-edge);
    border-radius: 3px;
    box-shadow: 0 8px 24px rgba(0,0,0,0.25);
    color: var(--text);
  }
  /* Small card 70mm x 28mm */
  .card-small { left: 50px; top: 340px; width: 550px; height: 220px; }
  /* Square card 65mm x 65mm */
  .card-square {
    left: 700px; top: 250px; width: 400px; height: 400px;
    display: flex; align-items: center; justify-content: center;
  }

  .brand-name {
    font-weight: 900;
    letter-spacing: 1px;
    line-height: 1;
  }
  .card-small .brand-name {
    position: absolute;
    top: 28px;
    left: 0;
    width: 100%;
    text-align: center;
    font-size: 54px;
    color: var(--green);
  }
  .card-square .brand-name {
    font-size: 64px;
    color: var(--silver);
  }

  .holder-name {
    position: absolute;
    top: 100px;
    left: 0;
    width: 100%;
    text-align: center;
    font-size: 18px;
    font-weight: 700;
    color: var(--green);
  }
  .details {
    position: absolute;
    top: 134px;
    left: 0;
    width: 100%;
    display: flex;
    justify-content: center;
    align-items: center;
    gap: 18px;
  }
  .address {
    font-size: 15px;
    line-height: 1.4;
    text-align: right;
  }
  .divider {
    width: 1px;
    height: 42px;
    background: var(--muted);
  }
  .contact { list-style: none; font-size: 15px; line-height: 1.4; }
  .contact li { display: flex; align-items: center; gap: 7px; }
  .contact svg { width: 13px; height: 13px; fill: var(--green); }
</style>
</head>
<body>
  <section class="card card-small">
    <div class="brand-name">TULMEX</div>
    <div class="holder-name">MARCUS HALE</div>
    <div class="details">
      <p class="address">421, Address line here<br>Country Name,45452</p>
      <span class="divider"></span>
      <ul class="contact">
        <li>
          <svg viewBox="0 0 16 16" aria-hidden="true"><path d="M1 5c0-2 3-3 7-3s7 1 7 3v1h-3V4.5H4V6H1z"/><path d="M3 7h10l1 7H2z"/></svg>
          444 555 0192
        </li>
        <li>
          <svg viewBox="0 0 16 16" aria-hidden="true"><path d="M1 3h14v10H1z M2 4l6 5 6-5" stroke="#0c0c0c" stroke-width="1"/></svg>
          info@tulmexmail.com
        </li>
      </ul>
    </div>
  </section>

  <section class="card card-square">
    <div class="brand-name">TULMEX</div>
  </section>
</body>
</html>
```